依頼詳細
利用先は3パターンとなり、それぞれでデザインを作成して頂きます。
<利用先>
・ポスティング(A4)
・事務所壁に設置するポスター(B0サイズ)
・車両に貼付けするマグネットシート(縦横30cm幅でバンの後ろに取付)※左右2枚に分けてか1枚に収まるでも可
記載項目
社名、求人条件https://jp.shigotomadoguchi.net/q-%E9%9B%BB%E6%B0%97%E5%B7%A5%E4%BA%8B%E5%A3%AB-l-%E5%85%B5%E5%BA%AB%E7%9C%8C-%E5%8A%A0%E5%8F%A4%E5%B7%9D%E5%B8%82-%E6%B1%82%E4%BA%BA.html?vjk=3f91c2b7d05e6a48&advn=2739481650274813

別途添付資料の分析表
サイズ
ポスティングA4、ポスターB0、マグネットシート縦横30cm
ページ数
片面
希望イメージ
シンプル 複雑
単色 カラフル
暗い 明るい
日常 高級
遊び心 厳粛
未来的 伝統的
女性的 男性的
希望する色
緑系、水色系
納品ファイル
• イラストレーター形式 (.ai)
補足説明

メッセージではご連絡させていただいておりましたが、非常にわかりやすいデザインで目が惹かれました。
よろしくお願いいたします。

この度はご提案いただき誠にありがとうございました。
皆さん非常に目の惹かれるデザインでしたが、社内にて検討の結果選定させていただきました。

また、今後依頼させていただくことも増える予定ですので機会がございましたらその際はよろしくお願いいたします。

```html
<!DOCTYPE html>
<html lang="ja">
<head>
<meta charset="utf-8">
<title>電気工事士 急募 | 株式会社AOBA</title>
<link rel="stylesheet" href="https://fonts.googleapis.com/css2?family=Noto+Sans+JP:wght@400;500;700;900&family=Noto+Serif+JP:wght@700;900&display=swap">
<style>
  :root {
    --sky-top: #5f9fd6;
    --sky-low: #b9d7ee;
    --mountain: #6e7d4c;
    --panel: #2d4f86;
    --roof: #8f9aa6;
    --roof-dark: #4f5f73;
    --green: #2f9a3c;
    --navy: #1c3f73;
    --red: #e0141e;
    --ink: #111111;
    --white: #ffffff;
    --footer: #24394a;
  }
  * { box-sizing: border-box; margin: 0; padding: 0; }
  html, body { width: 848px; height: 1200px; overflow: hidden; background: #ffffff; }
  body { font-family: "Noto Sans JP", sans-serif; color: var(--ink); }

  .poster { position: relative; width: 848px; height: 1200px; overflow: hidden; }

  .photo-solar {
    position: absolute; left: 0; top: 0; width: 848px; height: 470px;
    background: linear-gradient(180deg, var(--sky-top) 0%, var(--sky-low) 30%, var(--mountain) 38%, #55643a 48%, var(--panel) 56%, #3e6aa8 78%, #9fb3c4 100%);
  }
  .photo-roof {
    position: absolute; left: 0; top: 470px; width: 848px; height: 430px;
    background: linear-gradient(180deg, #d7dde3 0%, var(--roof) 35%, var(--roof-dark) 100%);
  }

  .work-types {
    position: absolute; right: 26px; top: 18px; text-align: right;
    font-family: "Noto Serif JP", serif; font-weight: 900; color: var(--white);
    font-size: 56px; line-height: 1.3;
    -webkit-text-stroke: 1.5px #1a2a3a;
    paint-order: stroke fill;
    text-shadow: 0 0 6px rgba(0,0,0,.55);
  }
  .work-types .small { font-size: 44px; }

  .location {
    position: absolute; right: 26px; top: 380px;
    font-family: "Noto Serif JP", serif; font-weight: 900; font-size: 52px;
    color: var(--white); letter-spacing: 2px;
    text-shadow: 0 0 5px #000, 0 0 10px rgba(0,0,0,.6);
  }

  .headline-band {
    position: absolute; left: 0; top: 470px; width: 848px; height: 150px;
    background: linear-gradient(180deg, rgba(255,255,255,.92) 0%, rgba(255,255,255,.85) 70%, rgba(255,255,255,0) 100%);
  }
  .experience {
    position: absolute; left: 150px; top: 470px;
    font-weight: 900; font-size: 24px; color: var(--red); white-space: nowrap;
  }
  .experience b { font-size: 34px; }
  .headline {
    position: absolute; left: 26px; top: 500px; white-space: nowrap;
    font-weight: 900; line-height: 1; display: flex; align-items: flex-end;
  }
  .headline .job { font-size: 84px; color: var(--ink); letter-spacing: 0; }
  .headline .urgent { margin-left: 14px; font-size: 108px; color: var(--red); letter-spacing: -2px; -webkit-text-stroke: 2px var(--white); paint-order: stroke fill; }

  .perks { position: absolute; left: 330px; top: 608px; display: flex; align-items: center; gap: 8px; white-space: nowrap; }
  .perk {
    background: var(--green); color: var(--white); font-weight: 900; font-size: 24px; line-height: 1.3;
    padding: 4px 10px; border-radius: 4px; white-space: nowrap;
  }
  .salary { font-weight: 900; font-size: 26px; color: var(--white); text-shadow: 0 0 4px #000; }

  .leave-time {
    position: absolute; left: 396px; top: 656px; width: 424px; height: 50px;
    background: var(--navy); color: var(--white);
    font-weight: 900; font-size: 34px; text-align: center; line-height: 50px;
    letter-spacing: 1px; white-space: nowrap;
  }

  .tagline {
    position: absolute; left: 320px; top: 736px; text-align: center;
    font-weight: 900; font-size: 34px; line-height: 1.35; color: var(--white);
    text-shadow: 0 0 4px #000, 0 0 8px rgba(0,0,0,.6); white-space: nowrap;
  }
  .cycle { position: absolute; left: 590px; top: 726px; width: 240px; height: 140px; }
  .cycle .word {
    position: absolute; font-weight: 900; font-size: 48px; line-height: 1; color: var(--white);
    text-shadow: 0 0 4px #000, 0 0 8px rgba(0,0,0,.6);
  }
  .cycle .work { left: 0; top: 8px; }
  .cycle .life { right: 0; top: 78px; }
  .cycle svg { position: absolute; left: 98px; top: 16px; }

  .requirements {
    position: absolute; left: 0; top: 900px; width: 848px; height: 300px;
    background: var(--footer); color: var(--white);
    padding: 16px 24px 0 24px;
  }
  .requirements h2 { font-size: 22px; font-weight: 900; margin-bottom: 6px; }
  .requirements dl { font-size: 14px; line-height: 1.6; width: 640px; }
  .requirements dl div { display: flex; }
  .requirements dt { flex: none; font-weight: 700; }
  .requirements dd { padding-left: 2px; }

  .site-note {
    position: absolute; right: 20px; top: 918px; width: 170px;
    font-size: 12px; color: var(--white); text-align: center; white-space: nowrap;
  }

  .company {
    position: absolute; left: 24px; bottom: 22px; display: flex; align-items: baseline; gap: 14px;
    color: var(--white); font-weight: 900; white-space: nowrap;
  }
  .company .small { font-size: 20px; }
  .company .name { font-size: 44px; letter-spacing: 1px; }
  .company .tel { font-size: 42px; }
</style>
</head>
<body>
<main class="poster">
  <div class="photo-solar" role="img" aria-label="山の斜面に並ぶ太陽光パネルと青空の写真"></div>
  <div class="photo-roof" role="img" aria-label="屋根の上で太陽光パネルの施工作業をする作業員の写真"></div>

  <p class="work-types">QB改造<br>電源結線<br>建柱<span class="small">等</span></p>
  <p class="location">兵庫県加古川市</p>

  <div class="headline-band"></div>
  <p class="experience"><b>5</b>年以上経験者</p>
  <h1 class="headline"><span class="job">電気工事士</span><span class="urgent">急募!!</span></h1>

  <div class="perks">
    <span class="perk">土日休み</span>
    <span class="perk">安定の月給制</span>
    <span class="salary">年収400万円~</span>
  </div>

  <p class="leave-time">平均18時に退社可能</p>

  <p class="tagline">自分の経験を<br>活かして変える</p>
  <div class="cycle">
    <span class="word work">仕事</span>
    <svg width="48" height="70" viewBox="0 0 48 70" aria-hidden="true">
      <path d="M26 6 C42 12 44 30 36 42" fill="none" stroke="var(--green)" stroke-width="7"/>
      <polygon points="26,40 44,36 40,54" fill="var(--green)"/>
      <path d="M22 64 C6 58 4 40 12 28" fill="none" stroke="var(--green)" stroke-width="7"/>
      <polygon points="22,30 4,34 8,16" fill="var(--green)"/>
    </svg>
    <span class="word life">生活</span>
  </div>

  <section class="requirements">
    <h2>■募集要項</h2>
    <dl>
      <div><dt>【募集職種】</dt><dd>電気工事士／経験5年以上</dd></div>
      <div><dt>【応募条件】</dt><dd>・電気工事経験5年以上・第一種電気工事士または第二種電気工事士の資格保持者</dd></div>
      <div><dt>【雇用形態】</dt><dd>正社員</dd></div>
      <div><dt>【給与】</dt><dd>月給：28万円〜50万円（経験年数5年以上）、50万円〜63万7千円（経験年数10年以上）<br>※経験・能力に応じて更新あり</dd></div>
      <div><dt>【勤務地】</dt><dd>兵庫県加古川市緑町2-14-8</dd></div>
    </dl>
  </section>
  <p class="site-note">詳しい求人サイトはこちら</p>

  <div class="company">
    <span class="small">株式会社</span>
    <span class="name">AOBA</span>
    <span class="tel">【TEL】079-000-4826</span>
  </div>
</main>
</body>
</html>
```